Stitch Haven web site

I have been running an online business for 6 years.
www.stitchhaven.com.au I specialise in ribbons, buttons and unique craft materials. I sell online to individuals and shops with seperate retail and wholesale sites. The web page I'd like redesigned is my retail site.

It needs a clean, fresh look. I've recently had a new logo designed (thanks pixel guild!) and want the web site to incorporate the new design and colour scheme of black and white. (new logo attached as a file)

I no longer want the page with the large image www.stitchhaven.com.au I want to have the first page as the retail shop homepage.
http://www.stitchhaven.com.au/index.php so this page needs to have all the links

I want to the look to be fresh, modern and clear. It needs to be quick to load.

Notes from my IT guru: They need to know that the following tend to remain static with just the content section changing on each page; Header Left column (but different in the cart) right column (if required) footer
Updates

Thanks for your designs. 1/3 of my users use mobile devices so please take that into consideration. I would like the logo to be incorporated into the design and be a prominent feature (most have just used it as a tiny image in the top left corner. I would like it to be larger and more prominent.  thanks                                   

Thanks to all the designers who have submitted. Can you please add  'Boutique craft supplies' near the logo. That is my tag line. Thanks

Target Market(s)

Crafty females of all ages

Industry/Entity Type

Business

Requirements
Must have
• links to;
blog
gallery
chatterbook
snapboard
wholesale
space for an image which I change approx every 2 weeks
about Stitch Haven
contact
privacy policy
terms and conditions
newsletter sign up
shipping info
product search
Nice to have
• I am not sure if I want product images on the homepage? I have attached a few images.
Should not have
• not too much colour - I hate the green border I have now

```html
<!DOCTYPE html>
<html lang="en">
<head>
<meta charset="utf-8">
<title>Stitch Haven – Boutique craft supplies</title>
<link rel="stylesheet" href="https://fonts.googleapis.com/css2?family=Crimson+Text:wght@400;600;700&family=Arimo:wght@400;700&display=swap">
<style>
:root{
  --canvas:#dcd5cb;
  --canvas-light:#e6e0d7;
  --panel:#ffffff;
  --ink:#222222;
  --ink-soft:#555555;
  --ink-mute:#8a8a8a;
  --nav:#7a7a7a;
  --dark:#2b2b2b;
  --dark-2:#1d1d1d;
  --tan:#c9a470;
  --brown:#a97b4b;
  --brown-light:#c79a65;
  --brown-dark:#5b3e22;
  --green:#6f9a2e;
  --footer:#272727;
  --footer-text:#c9c9c9;
}
*{box-sizing:border-box;margin:0;padding:0}
html,body{width:797px;height:1200px;overflow:hidden}
body{background:var(--canvas);font-family:"Arimo",Arial,sans-serif;color:var(--ink)}
.page{position:relative;width:797px;height:1200px;overflow:hidden;
  background:linear-gradient(var(--canvas-light) 0,var(--canvas-light) 48px,var(--canvas) 48px)}
.page::before{content:"";position:absolute;left:0;right:0;top:46px;border-top:1px dashed #c8c0b4}
a{color:inherit;text-decoration:none}

/* header */
.brand{position:absolute;left:84px;top:22px;display:flex;align-items:center;gap:10px}
.brand-dot{width:26px;height:26px;border-radius:50%;background:var(--dark-2)}
.brand-name{font-family:"Crimson Text",Georgia,serif;font-size:30px;font-weight:400;color:var(--dark-2);line-height:1}
.account-links{position:absolute;left:476px;top:15px;display:flex;gap:14px;
  font-family:"Crimson Text",Georgia,serif;font-size:11px;color:#444;white-space:nowrap}
.cart-tab{position:absolute;left:642px;top:0;width:72px;height:62px}
.cart-tab .items{position:absolute;left:0;right:0;top:28px;text-align:center;font-size:7px;color:#aaa}
.main-nav{position:absolute;top:68px;left:390px;width:324px;display:flex;justify-content:space-between;
  font-family:"Crimson Text",Georgia,serif;font-size:13.5px;color:var(--nav)}
.main-nav .current{color:var(--ink);border-bottom:1px solid var(--ink)}

/* content panel */
.panel{position:absolute;left:68px;top:103px;width:660px;height:909px;background:var(--panel);
  border-radius:3px;box-shadow:0 0 4px rgba(0,0,0,.18)}
.hero{position:absolute;left:83px;top:118px;width:631px;height:222px;border:2px solid #111;
  background:radial-gradient(ellipse at 25% 50%,#a3242c 0,rgba(163,36,44,0) 38%),
    radial-gradient(ellipse at 50% 60%,#c7919c 0,rgba(199,145,156,0) 40%),
    radial-gradient(ellipse at 82% 45%,#9fc05a 0,rgba(159,192,90,0) 42%),#f1eeee}
.hero-caption{position:absolute;left:60px;top:284px;width:412px;height:38px;
  background:linear-gradient(90deg,var(--brown),var(--brown-light));box-shadow:0 2px 3px rgba(0,0,0,.3);
  font-family:"Crimson Text",Georgia,serif;font-size:20px;color:#fff;line-height:38px;padding-left:16px;white-space:nowrap}
.hero-caption::after{content:"";position:absolute;left:0;top:38px;border-top:8px solid var(--brown-dark);border-left:10px solid transparent}
.hero-arrow{position:absolute;top:313px;width:18px;height:18px;border-radius:50%;background:var(--green)}

/* category bar */
.category-bar{position:absolute;left:61px;top:360px;width:676px;height:70px;
  background:linear-gradient(#383838,#1c1c1c);box-shadow:0 2px 3px rgba(0,0,0,.35)}
.category-bar::before,.category-bar::after{content:"";position:absolute;top:70px;border-top:8px solid #000}
.category-bar::before{left:0;border-left:10px solid transparent}
.category-bar::after{right:0;border-right:10px solid transparent}
.cat-arrow{position:absolute;top:26px;width:18px;height:18px;border-radius:50%;background:var(--tan)}
.cat{position:absolute;top:24px;display:flex;align-items:center;gap:10px;color:var(--tan);font-size:12px;white-space:nowrap}
.cat svg{display:block}
.cat-sep{position:absolute;top:12px;width:1px;height:46px;background:#4a4a4a;box-shadow:1px 0 0 #111}

/* intro columns */
.col-title{position:absolute;font-family:"Crimson Text",Georgia,serif;font-weight:700;font-size:14.5px;color:var(--ink)}
.copy{position:absolute;font-size:8px;line-height:12px;color:var(--ink-soft);overflow:hidden}
.copy-long{height:84px}
.copy-short{height:24px}
.read-more{position:absolute;font-size:8.6px;color:var(--ink);white-space:nowrap}
.col-rule{position:absolute;top:456px;height:132px;border-left:1px dotted #bbb}
.blog-meta{position:absolute;font-size:8.6px;color:var(--ink);white-space:nowrap}
.blog-meta b{font-weight:700}
.blog-rule{position:absolute;left:307px;top:525px;width:160px;border-top:1px dotted #999}
.quote{font-family:"Crimson Text",Georgia,serif;font-size:15px;color:#888;line-height:0;vertical-align:-3px}
.quote-open{position:absolute;left:525px;top:486px;font-family:"Crimson Text",Georgia,serif;font-size:22px;color:#888;line-height:1}

/* products */
.section-title{position:absolute;left:84px;font-family:"Crimson Text",Georgia,serif;font-weight:700;font-size:14.5px}
.section-rule{position:absolute;left:84px;width:630px;border-top:1px solid #e4e4e4}
.product{position:absolute;width:110px;text-align:center}
.product-shot{width:78px;height:78px;margin:0 auto;border-radius:8px}
.product-name{margin-top:6px;font-size:9px;font-weight:700;color:var(--ink)}
.product-from{margin-top:3px;font-size:8.6px;color:var(--ink-mute)}
.product-price{margin-top:3px;font-size:8.6px;color:var(--ink)}
.cart-strip{position:relative;width:100px;height:4px;margin:9px auto 0;background:#3a3a3a}
.add-to-cart{display:block;width:60px;height:18px;margin:0 auto;background:var(--dark);color:#fff;font-size:8.4px;line-height:17px}

/* footer */
.footer{position:absolute;left:0;top:1034px;width:797px;height:166px;background:var(--footer);border-top:3px solid #111;color:var(--footer-text)}
.f-title{position:absolute;top:29px;font-family:"Crimson Text",Georgia,serif;font-size:14px;font-weight:400;color:#e2e2e2}
.f-list{position:absolute;top:51px;list-style:none;font-size:8.6px;line-height:13px}
.f-list li::before{content:"";display:inline-block;width:3px;height:3px;background:#888;margin-right:7px;vertical-align:middle}
.f-text{position:absolute;font-size:8.6px;white-space:nowrap}
.f-input{position:absolute;left:358px;top:66px;width:132px;height:17px;background:#1a1a1a;border:1px solid #333;font-size:8px;color:#888;line-height:15px;padding-left:6px}
.f-button{position:absolute;left:358px;top:92px;width:43px;height:16px;background:#151515;border:1px solid #3a3a3a;border-radius:2px;font-size:8.5px;color:#ddd;text-align:center;line-height:14px}
.social{position:absolute;left:547px;display:flex;align-items:center;width:74px;justify-content:space-between;font-size:8.6px}
.social i{display:block;width:17px;height:17px;border-radius:50%;background:#f2f2f2}
.pay-card{position:absolute;left:671px;width:32px;height:19px;background:#f4f4f4;border-radius:2px;font-size:6.5px;font-weight:700;color:#333;text-align:center;line-height:19px}
.f-bottom-rule{position:absolute;left:0;right:0;top:132px;border-top:1px solid #383838}
.f-legal{position:absolute;left:83px;top:144px;font-size:8.6px;color:#ddd}
.f-copy{position:absolute;left:661px;top:144px;font-size:8.6px;color:#ddd}
</style>
</head>
<body>
<div class="page">

  <header>
    <a class="brand" href="#"><span class="brand-dot"></span><span class="brand-name">Stitch Haven</span></a>
    <nav class="account-links"><a href="#">My Account</a><a href="#">Checkout</a><a href="#">Log In</a></nav>
    <div class="cart-tab">
      <svg width="72" height="62" viewBox="0 0 72 62">
        <path d="M0 0H72V62L36 52L0 62Z" fill="#333"/>
        <path d="M26 9h4l3 10h11l2-7H31" fill="none" stroke="#ddd" stroke-width="1.6"/>
        <circle cx="34" cy="22" r="1.6" fill="#ddd"/><circle cx="43" cy="22" r="1.6" fill="#ddd"/>
      </svg>
      <div class="items">Items: 0</div>
    </div>
    <nav class="main-nav">
      <a class="current" href="#">Home</a><a href="#">Shop</a><a href="#">Wholesale</a><a href="#">Gallery</a><a href="#">Blog</a><a href="#">Contact</a>
    </nav>
  </header>

  <main>
    <div class="panel"></div>
    <div class="hero" role="img" aria-label="Feature photo of red, pink and green organza ribbon flowers with beaded centres"></div>
    <div class="hero-caption">I specialise in ribbons, and unique craft materials</div>
    <span class="hero-arrow" style="left:657px"></span>
    <span class="hero-arrow" style="left:682px"></span>

    <nav class="category-bar">
      <span class="cat-arrow" style="left:18px"></span>
      <a class="cat" href="#" style="left:66px">
        <svg width="22" height="22" viewBox="0 0 22 22"><circle cx="11" cy="11" r="10" fill="#fff"/><circle cx="8" cy="8" r="2" fill="#222"/><circle cx="14" cy="8" r="2" fill="#222"/><circle cx="8" cy="14" r="2" fill="#222"/><circle cx="14" cy="14" r="2" fill="#222"/></svg>Buttons</a>
      <span class="cat-sep" style="left:151px"></span>
      <a class="cat" href="#" style="left:168px">
        <svg width="20" height="24" viewBox="0 0 20 24"><ellipse cx="10" cy="12" rx="8" ry="10" fill="none" stroke="#fff" stroke-width="2"/><ellipse cx="10" cy="12" rx="4" ry="6" fill="none" stroke="#fff" stroke-width="1.2"/></svg>Lace</a>
      <span class="cat-sep" style="left:239px"></span>
      <a class="cat" href="#" style="left:262px">
        <svg width="28" height="22" viewBox="0 0 28 22"><path d="M2 5c8-4 16 4 24 0M2 11c8-4 16 4 24 0M2 17c8-4 16 4 24 0" fill="none" stroke="#fff" stroke-width="2.2"/></svg>Ribbons</a>
      <span class="cat-sep" style="left:354px"></span>
      <a class="cat" href="#" style="left:374px">
        <svg width="24" height="24" viewBox="0 0 24 24"><path d="M12 1l3 7 7 1-5 5 2 8-7-4-7 4 2-8-5-5 7-1z" fill="#fff"/><circle cx="12" cy="12" r="3" fill="#222"/></svg>Flowers and Leaves</a>
      <span class="cat-sep" style="left:520px"></span>
      <a class="cat" href="#" style="left:538px">
        <svg width="24" height="24" viewBox="0 0 24 24"><path d="M12 1l3 3 4-1 1 4 3 3-2 4 1 4-4 1-3 3-3-2-4 1-1-4-3-3 2-4-1-4 4-1z" fill="#fff"/><circle cx="12" cy="12" r="3.5" fill="#222"/></svg>Stickers</a>
      <span class="cat-arrow" style="left:640px"></span>
    </nav>

    <section>
      <h2 class="col-title" style="left:84px;top:454px">About Us</h2>
      <p class="copy copy-long" style="left:84px;top:480px;width:196px">Lorem ipsum dolor sit amet, consectetur adipisi ing el it, sed do eiusmod tempor incididunt ut laore et dolore magna aliqua. Ut enim ad mi nim vniam, quis nostrud exercitation ullamco labor is isi ut aliquip ex ea comm odo consequat. Duisaue irure dolor in reprehenderit in voluptate velitesse cillum dolore eufugiat nulla paria magna aliqua. Ut enim ad minim vniam.</p>
      <a class="read-more" href="#" style="left:84px;top:576px">Read More...</a>
    </section>
    <span class="col-rule" style="left:289px"></span>

    <section>
      <h2 class="col-title" style="left:307px;top:454px">Our Blog</h2>
      <div class="blog-meta" style="left:307px;top:480px">14 May 2013</div>
      <div class="blog-meta" style="left:419px;top:480px"><b>Lorem ipsum dolor</b></div>
      <p class="copy copy-short" style="left:307px;top:494px;width:182px">Lorem ipsum dolor sit amet, consectetur adipisi ing el it, sed do eiusmod tempor</p>
      <span class="blog-rule"></span>
      <div class="blog-meta" style="left:307px;top:534px">14 May 2013</div>
      <div class="blog-meta" style="left:419px;top:534px"><b>Lorem ipsum dolor</b></div>
      <p class="copy copy-short" style="left:307px;top:548px;width:182px">Lorem ipsum dolor sit amet, consectetur adipisi ing el it, sed do eiusmod tempor</p>
      <a class="read-more" href="#" style="left:307px;top:576px">Read More...</a>
    </section>
    <span class="col-rule" style="left:511px"></span>

    <section>
      <h2 class="col-title" style="left:527px;top:454px">Testimonial</h2>
      <span class="quote-open">&ldquo;</span>
      <p class="copy copy-long" style="left:538px;top:480px;width:180px">Lorem ipsum dolor sit amet, consectetur adipisi in it, sed do eiusmod tempor incididunt ut laore et dolore magna aliqua. Ut enim ad mi nim vniam, quis nostrud exercitation ullamco labor is isi ut aliquip ex ea comm odo consequat. Duisaue irure dolor in reprehenderit in voluptate velitesse cillum dolore paria magna aliqua. <span class="quote">&rdquo;</span></p>
      <div class="blog-meta" style="left:527px;top:576px">By: Lorem Ipsum</div>
    </section>

    <h2 class="section-title" style="top:609px">New Products</h2>
    <span class="section-rule" style="top:633px"></span>
    <div class="product" style="left:79px;top:642px">
      <div class="product-shot" role="img" aria-label="Assorted colourful craft buttons" style="background:radial-gradient(circle,#e8c14e 0,#5fa6cf 45%,#d8553f 75%,rgba(255,255,255,0) 76%)"></div>
      <div class="product-name">Lorem Ipsum</div><div class="product-from">From:</div><div class="product-price">50$.00</div>
      <div class="cart-strip"></div><a class="add-to-cart" href="#">Add to cart</a>
    </div>
    <div class="product" style="left:214px;top:642px">
      <div class="product-shot" role="img" aria-label="Roll of lavender ribbon" style="background:radial-gradient(circle,#c9bfce 0,#9b8ea3 50%,rgba(255,255,255,0) 72%)"></div>
      <div class="product-name">Lorem Ipsum</div><div class="product-from">From:</div><div class="product-price">50$.00</div>
      <div class="cart-strip"></div><a class="add-to-cart" href="#">Add to cart</a>
    </div>
    <div class="product" style="left:346px;top:642px">
      <div class="product-shot" role="img" aria-label="Sheet of blue and white craft stickers" style="background:linear-gradient(135deg,#d9e8f2,#5b8fc0 55%,#e9eef2)"></div>
      <div class="product-name">Lorem Ipsum</div><div class="product-from">From:</div><div class="product-price">50$.00</div>
      <div class="cart-strip"></div><a class="add-to-cart" href="#">Add to cart</a>
    </div>
    <div class="product" style="left:478px;top:642px">
      <div class="product-shot" role="img" aria-label="Pile of red flower beads" style="background:radial-gradient(ellipse,#e2343a 0,#b8141c 45%,rgba(255,255,255,0) 70%)"></div>
      <div class="product-name">Lorem Ipsum</div><div class="product-from">From:</div><div class="product-price">50$.00</div>
      <div class="cart-strip"></div><a class="add-to-cart" href="#">Add to cart</a>
    </div>
    <div class="product" style="left:610px;top:642px">
      <div class="product-shot" role="img" aria-label="Two rolls of light blue patterned washi tape" style="background:radial-gradient(ellipse,#8fd3ea 0,#4fb2d8 45%,rgba(255,255,255,0) 70%)"></div>
      <div class="product-name">Lorem Ipsum</div><div class="product-from">From:</div><div class="product-price">50$.00</div>
      <div class="cart-strip"></div><a class="add-to-cart" href="#">Add to cart</a>
    </div>

    <h2 class="section-title" style="top:810px">Feature Products</h2>
    <span class="section-rule" style="top:834px"></span>
    <div class="product" style="left:79px;top:842px">
      <div class="product-shot" role="img" aria-label="Sheet of blue and white craft stickers" style="background:linear-gradient(135deg,#d9e8f2,#5b8fc0 55%,#e9eef2)"></div>
      <div class="product-name">Lorem Ipsum</div><div class="product-from">From:</div><div class="product-price">50$.00</div>
      <div class="cart-strip"></div><a class="add-to-cart" href="#">Add to cart</a>
    </div>
    <div class="product" style="left:214px;top:842px">
      <div class="product-shot" role="img" aria-label="Assorted colourful craft buttons" style="background:radial-gradient(circle,#e8c14e 0,#5fa6cf 45%,#d8553f 75%,rgba(255,255,255,0) 76%)"></div>
      <div class="product-name">Lorem Ipsum</div><div class="product-from">From:</div><div class="product-price">50$.00</div>
      <div class="cart-strip"></div><a class="add-to-cart" href="#">Add to cart</a>
    </div>
    <div class="product" style="left:346px;top:842px">
      <div class="product-shot" role="img" aria-label="Roll of lavender ribbon" style="background:radial-gradient(circle,#c9bfce 0,#9b8ea3 50%,rgba(255,255,255,0) 72%)"></div>
      <div class="product-name">Lorem Ipsum</div><div class="product-from">From:</div><div class="product-price">50$.00</div>
      <div class="cart-strip"></div><a class="add-to-cart" href="#">Add to cart</a>
    </div>
    <div class="product" style="left:478px;top:842px">
      <div class="product-shot" role="img" aria-label="Two rolls of light blue patterned washi tape" style="background:radial-gradient(ellipse,#8fd3ea 0,#4fb2d8 45%,rgba(255,255,255,0) 70%)"></div>
      <div class="product-name">Lorem Ipsum</div><div class="product-from">From:</div><div class="product-price">50$.00</div>
      <div class="cart-strip"></div><a class="add-to-cart" href="#">Add to cart</a>
    </div>
    <div class="product" style="left:610px;top:842px">
      <div class="product-shot" role="img" aria-label="Pile of red flower beads" style="background:radial-gradient(ellipse,#e2343a 0,#b8141c 45%,rgba(255,255,255,0) 70%)"></div>
      <div class="product-name">Lorem Ipsum</div><div class="product-from">From:</div><div class="product-price">50$.00</div>
      <div class="cart-strip"></div><a class="add-to-cart" href="#">Add to cart</a>
    </div>
  </main>

  <footer class="footer">
    <h3 class="f-title" style="left:83px">Site Map</h3>
    <ul class="f-list" style="left:83px"><li>Home</li><li>Shop</li><li>Wholesale</li><li>Gallery</li><li>Blog</li></ul>
    <h3 class="f-title" style="left:185px">Shipping Info</h3>
    <ul class="f-list" style="left:185px"><li>Help/Customer Support</li><li>Shipping Rates &amp; Information</li><li>Returns</li><li>Terms of Use</li><li>Register/Inquiries</li></ul>
    <h3 class="f-title" style="left:358px">Newsletter</h3>
    <p class="f-text" style="left:358px;top:52px">Lorem ipsum dolor sit amet, cons rei.</p>
    <div class="f-input">Enter Your Email</div>
    <a class="f-button" href="#">Signup</a>
    <h3 class="f-title" style="left:547px">Follow Us</h3>
    <a class="social" href="#" style="top:51px">Chatterbook<i></i></a>
    <a class="social" href="#" style="top:75px">Chirpline<i></i></a>
    <a class="social" href="#" style="top:98px">Snapboard<i></i></a>
    <h3 class="f-title" style="left:671px">Payment</h3>
    <span class="pay-card" style="top:53px">Cardex</span>
    <span class="pay-card" style="top:78px">Paycircle</span>
    <span class="pay-card" style="top:104px">Walletly</span>
    <span class="f-bottom-rule"></span>
    <div class="f-legal"><a href="#">Privacy policy</a> &nbsp;|&nbsp; <a href="#">Terms and conditions</a></div>
    <div class="f-copy">Copyright 2013</div>
  </footer>

</div>
</body>
</html>
```